Contractor Business Card Design

Looking to have a card made that has a bold description of (KITCHENS, BASEMENTS, BATHROOMS)

Definition and layers a plus

Contact info is;

Mark T. Ellery
Shakopee, MN 55379
Cell: 612-555-0147
website: www.cobaltfinishworks.example
Email: cobaltfinishworksmn@mailbox.example

colors: red, black, gray, white

Contact Information for Business Card

Contact info is;

Mark T. Ellery
Shakopee, MN 55379
Cell: 612-555-0147

Colors
ec1f27

Requirements
Must have
• Looking for layers and definition
Nice to have
• Cards are planned to be printed on plastic cards

```html
<!DOCTYPE html>
<html lang="en">
<head>
<meta charset="utf-8">
<title>Cobalt Finish Works – Business Card</title>
<link rel="stylesheet" href="https://fonts.googleapis.com/css2?family=Oswald:wght@400;500&family=Montserrat:wght@400;500;700&display=swap">
<style>
  :root {
    --red: #ec1f27;
    --black: #000000;
    --charcoal: #2b2b2b;
    --gray: #b9b9bd;
    --white: #ffffff;
    --line-dark: #111111;
    --backdrop: #e6e6e6;
  }
  html, body {
    margin: 0;
    width: 960px;
    height: 1200px;
    overflow: hidden;
    background: var(--backdrop);
  }
  .canvas {
    position: relative;
    width: 960px;
    height: 1200px;
  }
  .card {
    position: absolute;
    left: 60px;
    width: 840px;
    height: 480px;
    overflow: hidden;
    background: radial-gradient(ellipse at 55% 45%, var(--charcoal) 0%, #111 55%, var(--black) 100%);
    box-shadow: 0 10px 24px rgba(0,0,0,0.25);
  }
  .card--front { top: 70px; }
  .card--back { top: 650px; }
  .card svg.card-shapes {
    position: absolute;
    inset: 0;
  }
  .services-title {
    position: absolute;
    left: 34px;
    top: 62px;
    margin: 0;
    font-family: "Oswald", sans-serif;
    font-weight: 400;
    font-size: 56px;
    line-height: 1;
    letter-spacing: -0.5px;
    color: var(--red);
    white-space: nowrap;
  }
  .brand-name {
    position: absolute;
    margin: 0;
    font-family: "Montserrat", sans-serif;
    font-weight: 700;
    color: var(--white);
    text-align: center;
    line-height: 1.05;
  }
  .brand-name .brand-main { display: block; }
  .brand-name .brand-sub { display: block; }
  .card--front .brand-name { left: 620px; top: 24px; width: 200px; }
  .card--front .brand-main { font-size: 34px; letter-spacing: 2px; }
  .card--front .brand-sub { font-size: 12px; letter-spacing: 6px; margin-top: 4px; }
  .card--back .brand-name { left: 590px; top: 232px; width: 230px; }
  .card--back .brand-main { font-size: 44px; letter-spacing: 2px; }
  .card--back .brand-sub { font-size: 15px; letter-spacing: 8px; margin-top: 6px; }

  .contact-name {
    position: absolute;
    left: 66px;
    top: 56px;
    margin: 0;
    font-family: "Oswald", sans-serif;
    font-weight: 400;
    font-size: 62px;
    line-height: 1;
    color: var(--gray);
    letter-spacing: -0.5px;
  }
  .contact-role {
    position: absolute;
    left: 100px;
    top: 140px;
    margin: 0;
    font-family: "Montserrat", sans-serif;
    font-weight: 400;
    font-size: 19px;
    color: var(--white);
    letter-spacing: 1px;
  }
  .contact-role .amp { color: var(--red); }
  .contact-phone {
    position: absolute;
    left: 56px;
    top: 200px;
    margin: 0;
    font-family: "Montserrat", sans-serif;
    font-weight: 500;
    font-size: 30px;
    color: var(--white);
    letter-spacing: 1px;
  }
  .contact-email {
    position: absolute;
    left: 52px;
    top: 256px;
    margin: 0;
    font-family: "Montserrat", sans-serif;
    font-weight: 400;
    font-size: 18px;
    color: var(--white);
    letter-spacing: 0.5px;
  }
  .contact-email .at { color: var(--red); }
  .band-services {
    position: absolute;
    left: 34px;
    top: 340px;
    margin: 0;
    font-family: "Oswald", sans-serif;
    font-weight: 500;
    font-size: 36px;
    line-height: 1;
    color: var(--black);
    white-space: nowrap;
    letter-spacing: -0.3px;
  }
  .band-website {
    position: absolute;
    left: 190px;
    top: 396px;
    margin: 0;
    font-family: "Montserrat", sans-serif;
    font-weight: 400;
    font-size: 16px;
    color: var(--black);
    letter-spacing: 1.5px;
  }
</style>
</head>
<body>
<main class="canvas">

  <section class="card card--front" aria-label="Card front">
    <svg class="card-shapes" width="840" height="480" viewBox="0 0 840 480">
      <defs>
        <linearGradient id="photoTone" x1="0" y1="0" x2="1" y2="1">
          <stop offset="0" stop-color="#c9c5c2"/>
          <stop offset="0.45" stop-color="#6e6864"/>
          <stop offset="1" stop-color="#2f2b29"/>
        </linearGradient>
      </defs>
      <polygon class="project-photo" role="img"
               aria-label="Black-and-white photo collage of a remodelled kitchen, a stone fireplace basement with TV, and a bathroom vanity"
               points="0,172 580,172 800,420 0,420" fill="url(#photoTone)"/>
      <polyline class="photo-frame" points="0,172 580,172 800,420 0,420"
                fill="none" stroke="var(--red)" stroke-width="5"/>
      <circle class="brand-ring" cx="722" cy="160" r="60" fill="none" stroke="var(--red)" stroke-width="6"/>
      <circle class="partner-badge" cx="132" cy="372" r="58" fill="#ececec" stroke="#1a1a1a" stroke-width="4"/>
    </svg>
    <h1 class="services-title">KITCHEN • BATH • BASEMENT</h1>
    <p class="brand-name"><span class="brand-main">COBALT</span><span class="brand-sub">FINISH WORKS</span></p>
  </section>

  <section class="card card--back" aria-label="Card back">
    <svg class="card-shapes" width="840" height="480" viewBox="0 0 840 480">
      <polygon class="service-band" points="0,312 730,312 830,462 0,462" fill="var(--red)"/>
      <polyline class="band-rule" points="0,326 716,326 808,450 0,450"
                fill="none" stroke="var(--line-dark)" stroke-width="3"/>
      <circle class="brand-ring" cx="705" cy="122" r="88" fill="none" stroke="var(--red)" stroke-width="7"/>
    </svg>
    <h2 class="contact-name">MARK T. ELLERY</h2>
    <p class="contact-role">- OWNER <span class="amp">&amp;</span> MANAGER -</p>
    <p class="contact-phone">(612) 555-0147</p>
    <p class="contact-email">COBALTFINISHWORKSMN<span class="at">@</span>MAILBOX.EXAMPLE</p>
    <p class="brand-name"><span class="brand-main">COBALT</span><span class="brand-sub">FINISH WORKS</span></p>
    <p class="band-services">KITCHEN • BATH • BASEMENT • INSTALLATION</p>
    <p class="band-website">WWW.COBALTFINISHWORKS.EXAMPLE</p>
  </section>

</main>
</body>
</html>
```